Website Design für Reinigungsunternehmen
Zielgruppe
Wir sind ein Reinigungsunternehmen, dass seit 2014 am Markt ist.
Was machen wir:
Das Angebot besteht darin, Räume nach dem IFSG (Infektionsschutzgesetz) und den Richtlinien des Werner Lasko Instituts mit ausgewählten Verfahren keimfrei zu bekommen.
Hygiene und prophylaktische Desinfektion sind für die Nutzung stark frequentierter Räume und Oberflächen gerade jetzt essentiell, denn die Ausbreitung von Viren und Bakterien kann auch durch präventive Maßnahmen eingedämmt werden.
Das Angebot ist, mit speziellen Reinigungsverfahren in Kombination mit Kaltverneblung ,die Räume fast vollständig von Keimen, Viren und Bakterien zu befreien.
So ist auch die Desinfektion von schwer zugänglichen Stellen und Gegenständen gewährleistet. Die eingesetzte Kaltnebeltechnologie wirkt in Verbindung mit Wasserstoffperoxid in verschiedenen Konzentrationen sowohl bakterizid, viruzid als auch fungizid. Wasserstoffperoxid wird rückstandsfrei abgebaut. Nach einer Einwirkzeit kann der behandelte, desinfizierte Raum sofort mechanisch gelüftet werden – ohne Material oder Umweltschäden zu riskieren.
Hier ein kurzes und erklärendes Video: https://klipvid.example/Qx7tmRwPaen
Aufgabenstellung
Die Website Soll maximal 3 Seiten haben.. Home (bzw. was wir machen..) Über uns (wer wir sind..) und Kontakt (-daten.
Ich möchte relativ kurz und knapp zum Thema kommen. Wenig Text, nur das wesentliche auf den Punkt gebracht - dafür ein ansprechendes professionelles Design. Bitte keine Bilder mit Gebäude, Reiniger etc. - dafür andere kreative Assoziationen einbringen.

```html
<!DOCTYPE html>
<html lang="de">
<head>
<meta charset="utf-8">
<title>orvel – Innovative Hygienekonzepte</title>
<link href="https://fonts.googleapis.com/css2?family=Montserrat:ital,wght@0,400;0,500;0,600;0,700;0,800;1,400&display=swap" rel="stylesheet">
<style>
:root{
  --blue:#034a93;
  --blue-soft:#4a7fb3;
  --green:#8bc540;
  --ink:#333;
  --muted:#c9c9c9;
  --footer:#3d3d3d;
  --white:#fff;
}
*{margin:0;padding:0;box-sizing:border-box}
html,body{width:1045px;height:1200px;overflow:hidden}
body{font-family:'Montserrat',sans-serif;background:#f6f7f9;position:relative;color:var(--ink)}
.abs{position:absolute}
.site-header{position:absolute;left:0;top:0;width:1045px;height:65px;background:var(--white);z-index:3}
.brand{position:absolute;left:204px;top:18px;display:flex;align-items:center;gap:6px}
.brand-dot{width:26px;height:26px;border-radius:50%;background:var(--blue)}
.brand-name{font-size:28px;font-weight:500;color:var(--blue);letter-spacing:-0.5px;line-height:1}
.nav a{position:absolute;top:30px;font-size:8.6px;font-weight:600;color:var(--ink);text-decoration:none}
.nav a.active{color:var(--green)}
.hero{position:absolute;left:0;top:65px;width:1045px;height:570px;overflow:hidden;
  background:linear-gradient(180deg,#f8f9fb 0%,#f3f5f8 100%)}
.hero-bg{position:absolute;left:0;top:0}
.hero-visual{position:absolute;left:430px;top:0;width:615px;height:560px;
  background:radial-gradient(ellipse at 62% 42%,rgba(78,140,232,.95) 0%,rgba(60,120,220,.6) 30%,rgba(3,74,147,0) 58%)}
.hero-water{position:absolute;left:0;top:300px;width:1045px;height:290px;
  background:linear-gradient(180deg,rgba(150,190,220,0) 0%,rgba(190,215,235,.55) 35%,rgba(245,247,250,.9) 75%,rgba(246,247,249,1) 100%)}
.hero-title{position:absolute;left:202px;top:90px;color:var(--white);font-weight:800;line-height:1}
.hero-title .big{display:block;font-size:57px;letter-spacing:-0.5px}
.hero-title .sub{display:block;font-size:32px;font-weight:700;margin-top:2px}
.btn{position:absolute;display:flex;align-items:center;justify-content:center;width:98px;height:27px;
  background:var(--green);color:var(--white);font-size:10px;font-weight:700;border-radius:4px;
  box-shadow:0 2px 3px rgba(0,0,0,.25);text-decoration:none}
.section-title{position:absolute;left:0;width:1045px;top:637px;text-align:center;font-size:28px;font-weight:800;color:var(--blue)}
.service-card{position:absolute;left:297px;top:696px;width:180px;height:180px;background:var(--blue);border-radius:6px}
.service-icon{position:absolute;left:34px;top:34px;width:112px;height:112px;border-radius:8px;background:rgba(255,255,255,.12)}
.service-title{position:absolute;left:531px;top:713px;font-size:16.5px;font-weight:800;color:var(--blue);line-height:1.08}
.service-text{position:absolute;left:531px;top:758px;width:225px;font-size:9.1px;line-height:10.5px;color:var(--ink)}
.features{position:absolute;left:529px;top:862px;display:flex;gap:12px;font-size:6.7px;color:var(--blue);align-items:center}
.features span{display:flex;align-items:center;gap:4px}
.arrow{position:absolute;top:772px}
.thumbs .thumb{position:absolute;top:910px;width:59px;height:59px;border-radius:4px;background:#d6d6d6}
.thumbs .thumb.active{background:var(--blue)}
.thumbs .thumb i{position:absolute;left:14px;top:14px;width:31px;height:31px;border-radius:4px;background:rgba(255,255,255,.3)}
.thumbs .label{position:absolute;top:977px;width:59px;text-align:center;font-size:9px;font-weight:600;color:var(--muted);white-space:nowrap}
.thumbs .label.active{color:var(--blue)}
.site-footer{position:absolute;left:0;top:1033px;width:1045px;height:167px;background:var(--footer);color:var(--white)}
.site-footer h4{position:absolute;top:32px;font-size:7.6px;font-weight:700}
.site-footer p,.site-footer li{font-size:8.2px;line-height:9px}
.footer-links li,.contact-list li{position:absolute;list-style:none;display:flex;align-items:center;gap:5px}
.newsletter{position:absolute;left:694px;top:50px;width:147px;height:27px;background:#d8d8d8;border-radius:4px}
.newsletter span{position:absolute;left:10px;top:9px;font-size:8px;font-style:italic;color:#888}
.newsletter svg{position:absolute;right:8px;top:9px}
.news-note{position:absolute;left:694px;top:87px;width:150px;font-size:6.6px!important;line-height:7.5px!important}
.divider{position:absolute;left:204px;top:139px;width:637px;height:1px;background:#5a5a5a}
.copyright{position:absolute;left:0;width:1045px;top:150px;text-align:center;font-size:6.3px;font-weight:500}
.copyright b{font-weight:800}
</style>
</head>
<body>
<header class="site-header">
  <div class="brand"><span class="brand-dot"></span><span class="brand-name">orvel</span></div>
  <nav class="nav">
    <a class="active" style="left:660px">HOME</a>
    <a style="left:719px">LEISTUNGEN</a>
    <a style="left:798px">KONTAKT</a>
  </nav>
</header>

<section class="hero">
  <svg class="hero-bg" width="1045" height="570" viewBox="0 0 1045 570">
    <path d="M0 0H1045V150C1000 330 900 450 780 455C640 460 560 380 470 350C360 315 250 300 160 330C90 352 40 380 0 405Z" fill="var(--blue)"/>
    <circle cx="70" cy="0" r="130" fill="var(--blue-soft)"/>
    <path d="M258 330A120 120 0 0 1 490 345C440 350 350 320 258 330Z" fill="var(--blue-soft)"/>
  </svg>
  <div class="hero-visual" role="img" aria-label="Blauer Schutzhandschuh, umgeben von spritzendem Wasser"></div>
  <div class="hero-water" role="img" aria-label="Geschwungene Wasserwelle mit Luftblasen"></div>
  <h1 class="hero-title"><span class="big">INNOVATIVE</span><span class="sub">HYGIENEKONZEPTE</span></h1>
  <a class="btn" style="left:204px;top:215px">LERN MEHR</a>
</section>

<h2 class="section-title">LEISTUNGEN</h2>

<svg class="arrow" style="left:243px" width="16" height="26" viewBox="0 0 16 26"><path d="M13 2L3 13L13 24" fill="none" stroke="#9a9a9a" stroke-width="4" stroke-linecap="round" stroke-linejoin="round"/></svg>
<svg class="arrow" style="left:786px" width="16" height="26" viewBox="0 0 16 26"><path d="M3 2L13 13L3 24" fill="none" stroke="#9a9a9a" stroke-width="4" stroke-linecap="round" stroke-linejoin="round"/></svg>

<div class="service-card"><div class="service-icon" role="img" aria-label="Symbol: Sprühflasche und wischende Hand"></div></div>
<h3 class="service-title">SCHEUER-WISCH-<br>DESINFEKTION</h3>
<p class="service-text">Lorem ipsum dolor sit amet, consectetur adipisc-ing elit, sed do eiusmod tempor incididunt ut labore et dolore magna aliqua. Ut enim ad minim veniam, quis nostrud exercitation ullamco laboris nisi ut aliquip ex ea commodo consequat.</p>
<a class="btn" style="left:531px;top:820px">LERN MEHR</a>
<div class="features">
  <span><svg width="11" height="12" viewBox="0 0 11 12"><circle cx="5.5" cy="6.5" r="4.5" fill="none" stroke="var(--blue)" stroke-width="1.2"/><path d="M5.5 6.5V4M4 1h3" stroke="var(--blue)" stroke-width="1.2"/></svg>168 STUNDE SCHUTZ</span>
  <span><svg width="10" height="12" viewBox="0 0 10 12"><path d="M5 1C1 5 1 9 5 11C9 9 9 5 5 1Z" fill="var(--blue)"/></svg>MENSCHENFREUNDLICH</span>
</div>

<div class="thumbs">
  <div class="thumb active" style="left:349px"><i></i></div>
  <div class="thumb" style="left:441px"><i></i></div>
  <div class="thumb" style="left:534px"><i></i></div>
  <div class="thumb" style="left:637px"><i></i></div>
  <div class="label active" style="left:349px">Lorem ipsum</div>
  <div class="label" style="left:441px">Lorem ipsum</div>
  <div class="label" style="left:534px">Lorem ipsum</div>
  <div class="label" style="left:637px">Lorem ipsum</div>
</div>

<footer class="site-footer">
  <h4 style="left:204px">ORVEL GROUP</h4>
  <p class="abs" style="left:204px;top:60px">Gebäudereinigung &amp; Hygienekonzepte<br>Lindenhofweg 4<br>89199 Bergwiesen</p>

  <h4 style="left:422px">QUICK LINKS</h4>
  <ul class="footer-links">
    <li style="left:422px;top:60px">HOME</li>
    <li style="left:422px;top:78px">LEISTUNGEN</li>
    <li style="left:422px;top:96px">KONTAKT</li>
  </ul>

  <h4 style="left:531px">KONTAKT UNS</h4>
  <ul class="contact-list">
    <li style="left:531px;top:60px"><svg width="10" height="10" viewBox="0 0 10 10"><path d="M2 0.5L4 3L3 4.3C3.8 5.8 4.6 6.6 5.9 7.2L7 6L9.5 8L8.5 9.5C4.5 9.3 0.8 5.5 0.5 1.5Z" fill="#fff"/></svg>07311 / 482 190 30</li>
    <li style="left:531px;top:78px"><svg width="10" height="10" viewBox="0 0 10 10"><rect x="2.5" y="0.5" width="5" height="4" fill="#fff"/><rect x="1" y="5" width="8" height="4.5" rx="1" fill="#fff"/></svg>07311 / 482 190 39</li>
    <li style="left:531px;top:96px"><svg width="10" height="8" viewBox="0 0 10 8"><rect width="10" height="8" rx="1" fill="#fff"/><path d="M0.5 1L5 4.5L9.5 1" fill="none" stroke="var(--footer)" stroke-width="1"/></svg>mail@orvel-gruppe.de</li>
  </ul>

  <h4 style="left:694px">NEWSLETTER</h4>
  <div class="newsletter"><span>Email address</span><svg width="10" height="8" viewBox="0 0 10 8"><rect width="10" height="8" rx="1" fill="#fff"/><path d="M0.5 1L5 4.5L9.5 1" fill="none" stroke="#d8d8d8" stroke-width="1"/></svg></div>
  <p class="news-note">Lorem ipsum dolor sit amet, consectetur adipiscing elit</p>

  <div class="divider"></div>
  <div class="copyright">ALL RIGHTS RESERVED BY <b>9FENNEL</b></div>
</footer>
</body>
</html>
```